STAFFONLYを変更
カメラをよりシンプルに
サイズの相談
ベースはこちらに決定いたします
ありがとうございます。
みなさまありがとうございます
最後まで悩みましたが
よりシンプルなもので
非関係者の抑制効果が一番ありそうなものを採用いたしました
関係者以外立ち入り禁止 POP POPデザインの仕事の依頼
MicrosoftAzureを中心にクラウドサービスを使った業務用アプリケーション開発をメインに行っております。
C#によるASP.NETによるWeb開発が中心で、WPFデスクトップアプリ、Formアプリ、Xamarinモバイルアプリを採用しております。
ミナトベルグでは上記プログラミングのパートナーを主に募集しています。
■募集に応募される方へのお願い
継続したお取引が可能な方を探しております。
フリーランス(一人法人含む)の方か、副業の方へご発注することが多いです。チームや法人、オフショアフロントの方と経験上成功したことがないです。
メッセージ中心のため、意図が伝わらず、容易に音信不通になります。実際に会うこともなくシステム上契約不履行時の違約金もないため、仕方がないことと割り切っていますが、大勢の方とのやり取りをしてメンバー選定しているので悲しくなります。逆にこちらからのレスが滞りご迷惑をおかけることもあります。
またプロトタイプで進めている関係で、要求がアバウトになることがほとんど。指示が二転三転することも。そういったことに神経質でない方がよいです。
トラブルで多いのが、資源を渡した瞬間に音信不通になる、成果物なしで支払いを余儀なくされる、生産的なやり取りではなく感情的なメッセージが来る、などです。こちらの作業内容や指示方法にも問題があることがありますので、初回の方は一定期間小規模予算でお互いが問題ないことを確認いただいてから継続契約します。
時々Skypeなどの打ち合わせを前提とされる方がおりますが、クラウドソーシングの特性を生かすとできるだけ時間を合わせて行うことが少ないほうが生産的で、必要最低限とさせて頂けますと幸いです。逆に作業時間帯はお好きな時間、何曜日でも構いません。フリーランスの方には十分な稼働時間を期待する半面、副業やフルで作業できないけど優れた技術者の開発リソースを安価に得られることがクラウドソーシングの最大のメリットだと考えています。
最後に、同じ自己紹介文で多くの仕事に同じメッセージで応募される方が多数おります。募集要項読んでいただけてない方は辞退しています。
いろいろ書いて申し訳ありませんが、私の考えに賛同してくださる方、ぜひ一緒に仕事させてください!
クライアント目線で柔軟な対応が可能な方と楽しく一緒に仕事をしたいです!

```html
<!DOCTYPE html>
<html lang="ja">
<head>
<meta charset="utf-8">
<title>MENBERS ONLY 関係者以外立入禁止 サイン</title>
<link href="https://fonts.googleapis.com/css2?family=Noto+Sans+JP:wght@500;700;900&display=swap" rel="stylesheet">
<style>
  :root {
    --sign-black: #0a0a0a;
    --sign-white: #ffffff;
    --alert-red: #d4151c;
    --page-bg: #f4f4f4;
    --outline-grey: #c9c9c9;
  }
  html, body {
    margin: 0;
    padding: 0;
    width: 1200px;
    height: 906px;
    overflow: hidden;
    background: var(--page-bg);
  }
  .sign-sheet {
    width: 1200px;
    height: 906px;
    display: flex;
    flex-direction: column;
    align-items: center;
    justify-content: center;
    gap: 58px;
  }
  .sign {
    display: block;
    width: 760px;
    height: 190px;
  }
  .sign--clear {
    background: var(--sign-white);
    outline: 1px dashed var(--outline-grey);
  }
  .sign-title {
    font-family: "Noto Sans JP", sans-serif;
    font-weight: 900;
    font-size: 66px;
    letter-spacing: 3px;
  }
  .sign-subtitle {
    font-family: "Noto Sans JP", sans-serif;
    font-weight: 700;
    font-size: 27px;
    letter-spacing: 1px;
  }
</style>
</head>
<body>
<main class="sign-sheet">

  <!-- Variant: solid black plate -->
  <svg class="sign sign--solid" viewBox="0 0 760 190" aria-label="MENBERS ONLY 関係者以外立入禁止">
    <rect width="760" height="190" fill="var(--sign-black)"/>
    <text class="sign-title" x="44" y="98" fill="var(--sign-white)">MENBERS ONLY</text>
    <rect x="34" y="112" width="692" height="5" fill="var(--sign-white)"/>
    <g class="camera-icon" fill="none" stroke="var(--sign-white)" stroke-width="4">
      <path d="M46 117 H104"/>
      <path d="M52 119 A23 23 0 0 0 98 119"/>
      <circle cx="75" cy="128" r="6"/>
    </g>
    <text class="sign-subtitle" x="722" y="155" text-anchor="end" fill="var(--sign-white)">関係者以外立入禁止</text>
  </svg>

  <!-- Variant: clear plate with black lettering -->
  <svg class="sign sign--clear" viewBox="0 0 760 190" aria-label="MENBERS ONLY 関係者以外立入禁止">
    <text class="sign-title" x="44" y="98" fill="var(--sign-black)">MENBERS ONLY</text>
    <rect x="34" y="112" width="692" height="5" fill="var(--sign-black)"/>
    <g class="camera-icon">
      <rect x="46" y="115" width="58" height="6" fill="var(--sign-black)"/>
      <path d="M52 119 A23 23 0 0 0 98 119 Z" fill="var(--sign-black)"/>
      <circle cx="75" cy="128" r="6" fill="var(--sign-white)"/>
    </g>
    <text class="sign-subtitle" x="722" y="155" text-anchor="end" fill="var(--sign-black)">関係者以外立入禁止</text>
  </svg>

  <!-- Variant: black plate with red prohibition stroke -->
  <svg class="sign sign--prohibit" viewBox="0 0 760 190" aria-label="MENBERS ONLY 関係者以外立入禁止">
    <rect width="760" height="190" fill="var(--sign-black)"/>
    <rect x="6" y="6" width="748" height="178" fill="none" stroke="var(--sign-white)" stroke-width="2"/>
    <line x1="6" y1="184" x2="754" y2="6" stroke="var(--alert-red)" stroke-width="4"/>
    <text class="sign-title" x="44" y="102" fill="var(--sign-white)">MENBERS ONLY</text>
    <rect x="34" y="116" width="692" height="5" fill="var(--sign-white)"/>
    <g class="camera-icon" fill="none" stroke="var(--sign-white)" stroke-width="4">
      <path d="M46 121 H104"/>
      <path d="M52 123 A23 23 0 0 0 98 123"/>
      <circle cx="75" cy="132" r="6"/>
    </g>
    <text class="sign-subtitle" x="722" y="159" text-anchor="end" fill="var(--sign-white)">関係者以外立入<tspan fill="var(--alert-red)">禁</tspan>止</text>
  </svg>

</main>
</body>
</html>
```